Fahrzeugbeschriftung für Elektrobetrieb
Zielgruppe
Von kleineren Elektro-Instandsetzungen /-reparaturen, über komplette Hausinstallationen, bis hin zu komplexeren Projekten sind wir Ihr kompetenter Ansprechpartner in Sachen Elektro
Aufgabenstellung
Powered by Henrik Vollmer soll mit drauf stehen und unsere Kontaktdaten für Ansbach und Bechhofen (07341-5928) siehe Internetseite www.strom-kerlinger.de
KD Modell R3 und R4 komplett verschlossen Farbe Blau
Danke :)

```html
<!DOCTYPE html>
<html lang="de">
<head>
<meta charset="utf-8">
<title>Fahrzeugbeschriftung – Strom Kerlinger</title>
<link rel="stylesheet" href="https://fonts.googleapis.com/css2?family=Montserrat:wght@300&family=Roboto:wght@500;700&display=swap">
<style>
  :root {
    --page: #e8eaec;
    --wrap-blue: #0a65a0;
    --wrap-blue-dark: #075585;
    --band-orange: #d04a17;
    --accent-orange: #e0562a;
    --white: #ffffff;
    --circle-grey: #c9ced4;
    --deco-light: #dde1e6;
    --deco-mid: #b4bcc6;
  }
  html, body {
    margin: 0;
    width: 1068px;
    height: 1200px;
    overflow: hidden;
    background: var(--page);
  }
  .canvas {
    position: relative;
    width: 1068px;
    height: 1200px;
  }
  .wrap-panel {
    position: absolute;
    left: 70px;
    top: 100px;
    width: 928px;
    height: 800px;
    border-radius: 60px 60px 24px 24px;
    background: linear-gradient(180deg, var(--wrap-blue) 0%, var(--wrap-blue) 80%, var(--wrap-blue-dark) 100%);
    overflow: hidden;
  }
  .deco-area {
    position: absolute;
    left: 518px;
    top: 0;
    width: 410px;
    height: 560px;
  }
  .website {
    position: absolute;
    left: 137px;
    top: 82px;
    margin: 0;
    font-family: "Montserrat", sans-serif;
    font-weight: 300;
    font-size: 21px;
    letter-spacing: 0.5px;
    color: var(--white);
    text-transform: uppercase;
  }
  .service-band {
    position: absolute;
    left: 0;
    top: 139px;
    width: 520px;
    height: 229px;
  }
  .service-list {
    position: absolute;
    left: 128px;
    top: 150px;
    margin: 0;
    padding: 0;
    list-style: none;
  }
  .service-item {
    display: flex;
    align-items: center;
    height: 70px;
    font-family: "Roboto", sans-serif;
    font-weight: 700;
    font-size: 31px;
    color: var(--white);
  }
  .service-icon {
    width: 52px;
    height: 52px;
    margin-right: 10px;
    flex: none;
  }
  .company-lockup {
    position: absolute;
    left: 124px;
    top: 632px;
    width: 208px;
  }
  .company-prefix {
    display: block;
    text-align: right;
    font-family: "Roboto", sans-serif;
    font-weight: 500;
    font-size: 24px;
    line-height: 1;
    color: var(--accent-orange);
  }
  .company-name {
    display: block;
    font-family: "Roboto", sans-serif;
    font-weight: 700;
    font-size: 33px;
    line-height: 1.05;
    letter-spacing: 2.6px;
    color: var(--white);
    white-space: nowrap;
  }
  .company-legal {
    display: block;
    text-align: right;
    font-family: "Roboto", sans-serif;
    font-weight: 500;
    font-size: 12.5px;
    color: var(--white);
    white-space: nowrap;
  }
  .company-dot {
    position: absolute;
    left: 338px;
    top: 652px;
    width: 44px;
    height: 44px;
    border-radius: 50%;
    background: var(--circle-grey);
  }
  .contact {
    position: absolute;
    right: 130px;
    top: 638px;
    margin: 0;
    font-style: normal;
    text-align: right;
    font-family: "Roboto", sans-serif;
    font-weight: 500;
    font-size: 21px;
    line-height: 25px;
    color: var(--white);
  }
</style>
</head>
<body>
<main class="canvas">
  <section class="wrap-panel">
    <svg class="deco-area" viewBox="0 0 410 560" role="img" aria-label="Große dekorative Grafikfläche in Grau und Orange">
      <defs>
        <linearGradient id="deco-fade" x1="0" x2="1" y1="1" y2="0">
          <stop offset="0" stop-color="#b4bcc6"/>
          <stop offset="0.55" stop-color="#dde1e6"/>
          <stop offset="1" stop-color="#c65a2a"/>
        </linearGradient>
      </defs>
      <path d="M150 0 H410 V560 H190 Q20 420 70 150 Q95 50 150 0 Z" fill="url(#deco-fade)" opacity="0.9"/>
    </svg>

    <p class="website">www.strom-kerlinger.de</p>

    <svg class="service-band" viewBox="0 0 520 229" aria-hidden="true">
      <defs>
        <linearGradient id="band-fade" x1="0" x2="1" y1="0" y2="0">
          <stop offset="0" stop-color="#d04a17" stop-opacity="0.15"/>
          <stop offset="0.16" stop-color="#d04a17" stop-opacity="1"/>
          <stop offset="1" stop-color="#d04a17"/>
        </linearGradient>
      </defs>
      <path d="M0 0 H495 Q470 110 497 229 H0 Z" fill="url(#band-fade)"/>
    </svg>

    <ul class="service-list">
      <li class="service-item">
        <svg class="service-icon" viewBox="0 0 52 52" fill="none" stroke="#fff" stroke-width="2">
          <path d="M14 4v14M38 4v14M8 18h36v16a6 6 0 0 1-6 6H14a6 6 0 0 1-6-6Z"/>
          <circle cx="26" cy="30" r="5"/>
          <path d="M20 40v6h12v-6"/>
        </svg>
        Elektroinstallation
      </li>
      <li class="service-item">
        <svg class="service-icon" viewBox="0 0 52 52" fill="none" stroke="#fff" stroke-width="2">
          <path d="M3 26 26 4l23 22M8 22v26h36V22M21 48V34h10v14M36 10v-4h5v9"/>
        </svg>
        Hausinstallation
      </li>
      <li class="service-item">
        <svg class="service-icon" viewBox="0 0 52 52" fill="none" stroke="#fff" stroke-width="2">
          <path d="M10 8c-6 4-6 12 2 22s18 16 24 14c2-1 4-3 4-5l-7-6-4 3c-4-2-9-7-11-11l3-4-6-8c-2 0-4 1-5 2Z"/>
          <path d="M22 6a22 22 0 1 1 14 40"/>
          <text x="30" y="26" fill="#fff" stroke="none" font-family="Roboto, sans-serif" font-size="14" font-weight="500" text-anchor="middle">24</text>
        </svg>
        Kundendienste
      </li>
    </ul>

    <div class="company-lockup">
      <span class="company-prefix">strom</span>
      <span class="company-name">KERLINGER</span>
      <span class="company-legal">powered by Henrik Vollmer</span>
    </div>
    <span class="company-dot" aria-hidden="true"></span>

    <address class="contact">
      Mühlgasse 12<br>
      91522 Ansbach<br>
      Tel.: 07341-5928
    </address>
  </section>
</main>
</body>
</html>
```